Plumber needs a business card

I need a new business card for my plumbing business. I dont have a logo at the moment but I want business cards that are simple but very professional. I want to look like
Name: Mitch Dorley
Address: (just make one up)
Phone: 0455 318 726
Email: mitch@dorleymail.com
Colors to use:
Blacks, blues, silvers

```html
<!DOCTYPE html>
<html lang="en">
<head>
<meta charset="utf-8">
<title>Mitch Dorley – Plumbing Contractor Business Card</title>
<link rel="stylesheet" href="https://fonts.googleapis.com/css2?family=Open+Sans:wght@400;700&display=swap">
<style>
  :root {
    --backdrop: #2b2c2e;
    --card-white: #ffffff;
    --panel-top: #ececec;
    --panel-bottom: #f8f8f8;
    --ink: #111111;
    --ink-soft: #2a2a2a;
    --brand-blue: #1777bd;
    --on-blue: #ffffff;
    --silver-light: #eef0f2;
    --silver-mid: #b9bec4;
    --silver-dark: #7d838a;
  }
  * { margin: 0; padding: 0; box-sizing: border-box; }
  html, body {
    width: 1200px;
    height: 750px;
    overflow: hidden;
    background: var(--backdrop);
    font-family: "Open Sans", Arial, sans-serif;
  }
  .card {
    position: absolute;
    left: 100px;
    top: 75px;
    width: 1000px;
    height: 600px;
    background: var(--card-white);
    overflow: hidden;
  }
  .card__panel {
    position: absolute;
    left: 28px;
    right: 28px;
    top: 28px;
    height: 360px;
    background: linear-gradient(180deg, var(--panel-top), var(--panel-bottom));
  }
  .card__valve-art {
    position: absolute;
    left: 50px;
    top: 107px;
    width: 145px;
    height: 160px;
    border-radius: 10px;
    background: radial-gradient(ellipse at 45% 40%, var(--silver-light), var(--silver-mid) 60%, var(--silver-dark));
  }
  .card__identity {
    position: absolute;
    left: 224px;
    top: 166px;
    color: var(--ink);
  }
  .card__name {
    font-size: 46px;
    line-height: 1;
    font-weight: 400;
    letter-spacing: 0.5px;
  }
  .card__name strong { font-weight: 700; }
  .card__role {
    margin-top: 6px;
    font-size: 26px;
    line-height: 1.1;
    color: var(--ink-soft);
  }
  .card__pipe-art {
    position: absolute;
    left: 0;
    top: 374px;
    width: 1000px;
    height: 32px;
    background: linear-gradient(180deg, var(--silver-dark), var(--silver-light) 35%, var(--silver-mid) 65%, var(--silver-dark));
  }
  .card__band {
    position: absolute;
    left: 0;
    right: 0;
    top: 406px;
    bottom: 0;
    background: var(--brand-blue);
    color: var(--on-blue);
  }
  .contact {
    position: absolute;
    font-size: 26px;
    line-height: 36px;
  }
  .contact strong { font-weight: 700; }
  .contact--address { left: 50px; top: 26px; }
  .contact--email { left: 50px; top: 116px; }
  .contact--phone {
    right: 46px;
    top: 70px;
    text-align: right;
  }
  .contact__label { display: block; font-weight: 700; font-size: 26px; line-height: 30px; }
  .contact__number { display: block; font-size: 37px; line-height: 46px; }
</style>
</head>
<body>
  <div class="card">
    <div class="card__panel"></div>
    <div class="card__valve-art" role="img" aria-label="Illustration of a silver pipe valve"></div>
    <div class="card__identity">
      <h1 class="card__name">MITCH <strong>DORLEY</strong></h1>
      <p class="card__role">Plumbing Contractor</p>
    </div>

    <div class="card__pipe-art" role="img" aria-label="Illustration of a silver pipe with couplings running across the card"></div>

    <div class="card__band">
      <p class="contact contact--address"><strong>ADDRESS:</strong> 1234 Street Address,<br>City Name, State Zip, Country</p>
      <p class="contact contact--email"><strong>EMAIL:</strong> mitch@dorleymail.com</p>
      <p class="contact contact--phone">
        <span class="contact__label">PHONE:</span>
        <span class="contact__number">0455 318 726</span>
      </p>
    </div>
  </div>
</body>
</html>
```